(Wix) Website Design Tweaks

The site: www.LanternAndLoomly.com
(The coding must be done within Wix. I will create a duplicate website so you can gain access and begin editing.)

My website contains my preferred text and images - but it needs to look more professional. My business focuses on "Corporate Messaging" and "Marketing Communications", so the website needs to look professional, but not too corporate. My clients range from very big companies to technology startups - the look and feel should be uncluttered, professional, and modern.

I want someone to review the pages, and make changes / suggestions focused on:
1) Fonts
2) Colors
3) Layout

If you have ideas for adding additional graphics, that's fine, but they should be consistent with what I already have . . . unless you think some / all of my images need to be changed.

My site is very, very small, and only contains 5 (very short) pages. There are no sub-pages. (One page is the contact page, with almost nothing except form fields.)

If you do a good job with my site, I may be able to provide you with additional work - many of my clients need website design tweaks, after I provide the verbiage.

```html
<!DOCTYPE html>
<html lang="en">
<head>
<meta charset="utf-8">
<title>Lantern &amp; Loomly</title>
<link href="https://fonts.googleapis.com/css2?family=Montserrat:wght@400;500;600;700&display=swap" rel="stylesheet">
<style>
:root{
  --blue:#1a8ce6;
  --blue-bright:#1f9bef;
  --brand-box:#10a6e8;
  --navy:#0d2552;
  --ink:#1b1f2b;
  --text:#2b2f3a;
  --mist:#eef1f7;
  --white:#ffffff;
  --footer-line:#2b4678;
}
*{margin:0;padding:0;box-sizing:border-box}
html,body{width:1200px;height:3728px;overflow:hidden}
body{font-family:'Montserrat',sans-serif;color:var(--text);background:var(--white);position:relative}
.abs{position:absolute}

/* header */
.site-header{position:absolute;left:0;top:0;width:1200px;height:75px;background:var(--white);z-index:3}
.brand-box{position:absolute;left:137px;top:0;width:123px;height:109px;background:var(--brand-box);color:var(--white);font-size:19px;line-height:24px;padding:54px 0 0 10px;font-weight:500;letter-spacing:.3px}
.main-nav a{position:absolute;top:29px;font-size:14px;color:#6b7180;text-decoration:none;letter-spacing:.4px}
.main-nav a.active{color:var(--blue-bright)}
.main-nav a.active::after{content:"";position:absolute;left:-10px;right:-10px;top:39px;height:4px;background:var(--blue-bright)}

/* hero */
.hero{position:absolute;left:0;top:75px;width:1200px;height:623px}
.hero-bg{position:absolute;inset:0;background:radial-gradient(circle at 71% 40%,#3fb4ff 0,#1268c4 14%,#0b2f6b 34%,#061a42 65%,#04122f 100%)}
.hero h1{position:absolute;left:126px;top:186px;color:var(--white);font-weight:500;font-size:47px;line-height:48px;letter-spacing:.5px}
.hero p{position:absolute;left:130px;top:296px;width:410px;color:#e6ecf7;font-size:14px;line-height:23px}
.btn{display:block;position:absolute;width:152px;height:39px;background:linear-gradient(90deg,#1572de,#2aa0f2);color:var(--white);font-size:12px;font-weight:600;text-align:center;line-height:39px;letter-spacing:.3px}
.hero .btn{left:130px;top:364px}
.scroll-mouse{position:absolute;left:589px;top:560px}

/* challenge */
.challenge{position:absolute;left:0;top:698px;width:1200px;height:579px}
.challenge .hex{position:absolute;left:108px;top:76px}
.section-title{font-size:34px;font-weight:500;color:var(--ink);letter-spacing:.3px}
.section-title b{font-weight:700;color:var(--blue-bright)}
.challenge .section-title{position:absolute;left:631px;top:107px}
.challenge .copy{position:absolute;left:637px;top:180px;width:450px;font-size:15px;line-height:23px}
.challenge .copy p+p{margin-top:34px}
.challenge .btn{left:637px;top:427px}

/* help */
.help{position:absolute;left:0;top:1277px;width:1200px;height:573px;background:linear-gradient(120deg,#eef1f7 0%,#e7ebf4 50%,#eef1f8 100%)}
.eyebrow{font-size:15px;color:var(--blue);letter-spacing:.4px}
.help .eyebrow{position:absolute;left:135px;top:127px}
.help .section-title{position:absolute;left:135px;top:148px;font-size:32px}
.rule{position:absolute;height:3px;background:var(--blue-bright)}
.help .copy{position:absolute;left:137px;top:221px;width:400px;font-size:15px;line-height:23px}
.help .copy p+p{margin-top:6px}
.help-card{position:absolute;width:209px;height:171px;background:var(--white)}
.help-card svg{position:absolute;left:20px;top:40px}
.help-card span{position:absolute;left:20px;bottom:30px;font-size:13px;font-weight:600;color:var(--navy);line-height:16px}
.help-card::before{content:"";position:absolute;left:0;bottom:28px;width:3px;height:36px;background:var(--blue-bright)}

/* expertise */
.expertise{position:absolute;left:0;top:1850px;width:1200px;height:638px;color:var(--white)}
.expertise-bg{position:absolute;inset:0;background:linear-gradient(100deg,#0c3a86 0%,#0b4ea9 45%,#0d63cc 75%,#1678db 100%)}
.expertise .eyebrow{position:absolute;left:0;width:1189px;top:66px;text-align:center;color:var(--white)}
.expertise .section-title{position:absolute;left:0;width:1189px;top:84px;text-align:center;color:var(--white)}
.expertise .section-title b{color:var(--white)}
.skill-grid{position:absolute;left:164px;top:184px;display:grid;grid-template-columns:repeat(4,213px);grid-auto-rows:150px;gap:12px 9px}
.skill{border:1px solid rgba(255,255,255,.22);display:flex;flex-direction:column;align-items:center;justify-content:center;text-align:center;font-size:15px;font-weight:500;line-height:19px}
.skill.active{border:2px solid var(--white)}
.skill svg{margin-bottom:12px}

/* clients */
.clients{position:absolute;left:0;top:2488px;width:1200px;height:371px}
.clients .section-title{position:absolute;left:0;width:1189px;top:70px;text-align:center}
.client{position:absolute;top:200px;transform:translateX(-50%);display:flex;align-items:center;gap:6px;font-size:17px;font-weight:600;color:#3d4352;white-space:nowrap}
.client i{display:block;width:12px;height:12px;border-radius:50%;background:var(--blue-bright)}
.arrow{position:absolute;top:204px}

/* results */
.results{position:absolute;left:0;top:2859px;width:1200px;height:535px;background:var(--mist)}
.results .photo{position:absolute;left:0;top:0;width:651px;height:535px;background:linear-gradient(135deg,#113a7a 0%,#1c5fb0 40%,#3b8bd6 60%,#0e2d60 100%);clip-path:polygon(0 0,536px 0,651px 268px,536px 535px,0 535px)}
.results .edge{position:absolute;left:0;top:0}
.results .section-title{position:absolute;left:700px;top:128px}
.results .copy{position:absolute;left:706px;top:212px;width:420px;font-size:16px;line-height:26.5px}
.results .copy p+p{margin-top:6px}

/* footer */
.site-footer{position:absolute;left:0;top:3394px;width:1200px;height:334px;background:var(--navy);color:var(--white)}
.footer-divider{position:absolute;top:0;width:1px;height:334px;background:var(--footer-line)}
.footer-mark{position:absolute;top:72px;width:3px;height:24px;background:var(--white)}
.footer-brand{position:absolute;left:159px;top:73px;font-size:20px;font-weight:500;letter-spacing:.5px}
.footer-about{position:absolute;left:159px;top:122px;width:260px;font-size:10px;line-height:15px;color:#b9c4da}
.footer-copy{position:absolute;left:159px;top:193px;font-size:10.5px;color:#d5dcea}
.footer-col{position:absolute;top:76px}
.footer-col h4{font-size:13px;font-weight:700;letter-spacing:.4px;margin-bottom:16px}
.footer-col a{display:block;font-size:11.5px;color:#c3cde0;text-decoration:none;margin-bottom:14px}
.social{display:flex;gap:8px;flex-wrap:wrap;width:220px}
.social span{display:flex;align-items:center;gap:4px;font-size:11px;font-weight:600}
.social i{display:block;width:10px;height:10px;border-radius:50%;background:var(--white)}
</style>
</head>
<body>

<header class="site-header">
  <div class="brand-box">LANTERN &amp;<br>LOOMLY</div>
  <nav class="main-nav">
    <a href="#" class="active" style="left:362px">HOME</a>
    <a href="#" style="left:488px">ABOUT US</a>
    <a href="#" style="left:646px">TESTIMONIALS</a>
    <a href="#" style="left:834px">TEAM</a>
    <a href="#" style="left:955px">CONTACT</a>
  </nav>
</header>

<section class="hero">
  <div class="hero-bg" role="img" aria-label="Glowing digital globe with network lines touched by a hand over a night city"></div>
  <h1>INFORM.<br>INFLUENCE. SELL.</h1>
  <p>In today’s competitive business environment, effective communication is more essential than ever before.</p>
  <a class="btn" href="#">LEARN MORE</a>
  <svg class="scroll-mouse" width="20" height="46" viewBox="0 0 20 46" fill="none" stroke="#fff" stroke-width="1.6">
    <rect x="2" y="1" width="16" height="25" rx="8"/><line x1="10" y1="6" x2="10" y2="11"/>
    <polyline points="5,31 10,36 15,31"/><polyline points="5,37 10,42 15,37"/>
  </svg>
</section>

<section class="challenge">
  <svg class="hex" width="482" height="416" viewBox="0 0 482 416">
    <defs><linearGradient id="hexFill" x1="0" y1="0" x2="1" y2="1"><stop offset="0" stop-color="#e9edf2"/><stop offset=".6" stop-color="#c9d2dc"/><stop offset="1" stop-color="#8fa2b8"/></linearGradient></defs>
    <polygon points="121,2 361,2 480,208 361,414 121,414 2,208" fill="none" stroke="#1f9bef" stroke-width="1.6"/>
    <polygon role="img" aria-label="Presenter at a flip chart speaking to a seated team in a bright office" points="132,12 350,12 460,208 350,404 132,404 22,208" fill="url(#hexFill)"/>
  </svg>
  <h2 class="section-title">THE BIG <b>CHALLENGE</b></h2>
  <div class="copy">
    <p>In today’s competitive business environment, effective communication is more essential than ever before. It is the foundation upon which companies are built, careers are propelled, and knowledge is imparted.</p>
    <p>Effective communication is critical - without it, misunderstandings arise, errors occur, and business goals are frustrated. In short, effective communication is the key driver of long-term business and professional success.</p>
  </div>
  <a class="btn" href="#">LEARN MORE</a>
</section>

<section class="help">
  <div class="eyebrow">WHY WE ARE</div>
  <h2 class="section-title">HOW CAN <b>WE HELP</b></h2>
  <div class="rule" style="left:137px;top:191px;width:63px"></div>
  <div class="copy">
    <p>At Lantern &amp; Loomly, we help individuals and organizations “get what they want” through clear and persuasive communication.</p>
    <p>Our consulting, coaching, and training services help clients achieve targeted business objectives, with an emphasis on informing, influencing, and selling.</p>
  </div>

  <div class="help-card" style="left:606px;top:85px">
    <svg width="50" height="48" fill="none" stroke="#1f9bef" stroke-width="1.6"><circle cx="25" cy="24" r="20" stroke-dasharray="4 3"/><rect x="15" y="16" width="20" height="13" rx="3"/></svg>
    <span>CLEAR &amp; PERSUASIVE<br>COMMUNICATION</span>
  </div>
  <div class="help-card" style="left:835px;top:134px">
    <svg width="50" height="48" fill="none" stroke="#1f9bef" stroke-width="1.6"><rect x="4" y="6" width="36" height="24"/><polyline points="8,24 16,16 24,20 34,10"/><line x1="10" y1="40" x2="40" y2="40"/></svg>
    <span>CONSULTING &amp;<br>TRAINING</span>
  </div>
  <div class="help-card" style="left:606px;top:276px">
    <svg width="50" height="52" fill="none" stroke="#1f9bef" stroke-width="1.6"><circle cx="16" cy="20" r="7"/><circle cx="36" cy="14" r="6"/><path d="M4 48v-10a12 12 0 0 1 24 0v10M26 48v-12a10 10 0 0 1 20 0v12"/></svg>
    <span>COACHING<br>SERVICE</span>
  </div>
  <div class="help-card" style="left:835px;top:324px">
    <svg width="50" height="50" fill="none" stroke="#1f9bef" stroke-width="1.6"><circle cx="22" cy="26" r="18"/><circle cx="22" cy="26" r="11"/><circle cx="22" cy="26" r="4"/><line x1="22" y1="26" x2="42" y2="6"/></svg>
    <span>HELP TO ACHIEVE<br>TARGETS</span>
  </div>
</section>

<section class="expertise">
  <div class="expertise-bg" role="img" aria-label="Audience seated at a conference under a blue tint"></div>
  <div class="eyebrow">WHAT WE DO</div>
  <h2 class="section-title">OUR <b>EXPERTISE</b></h2>
  <div class="rule" style="left:563px;top:136px;width:62px;background:#3ea9f5"></div>
  <div class="skill-grid">
    <div class="skill active"><svg width="48" height="42" fill="none" stroke="#fff" stroke-width="1.5"><rect x="16" y="2" width="28" height="18"/><circle cx="8" cy="12" r="4"/><path d="M4 40V22h8v18"/><circle cx="24" cy="30" r="3"/><circle cx="36" cy="30" r="3"/><line x1="18" y1="40" x2="44" y2="40"/></svg>Sales Training</div>
    <div class="skill"><svg width="48" height="42" fill="none" stroke="#fff" stroke-width="1.5"><circle cx="24" cy="21" r="8"/><circle cx="8" cy="8" r="4"/><circle cx="40" cy="8" r="4"/><circle cx="8" cy="34" r="4"/><circle cx="40" cy="34" r="4"/><path d="M11 11l7 5M37 11l-7 5M11 31l7-5M37 31l-7-5"/></svg>Marketing Collateral</div>
    <div class="skill"><svg width="48" height="42" fill="none" stroke="#fff" stroke-width="1.5"><rect x="6" y="4" width="30" height="22"/><polyline points="10,20 18,12 24,16 32,8"/><circle cx="36" cy="28" r="5"/><path d="M28 40a8 8 0 0 1 16 0"/></svg>Presentation Skills<br>Training</div>
    <div class="skill"><svg width="48" height="42" fill="none" stroke="#fff" stroke-width="1.5"><rect x="8" y="4" width="32" height="24"/><rect x="14" y="10" width="20" height="12"/><line x1="24" y1="28" x2="24" y2="36"/><line x1="14" y1="36" x2="34" y2="36"/></svg>Corporate &amp; Website<br>Messaging</div>
    <div class="skill"><svg width="48" height="42" fill="none" stroke="#fff" stroke-width="1.5"><path d="M6 6h24v16H14l-6 5v-5H6z"/><path d="M22 20h20v14h-4v5l-6-5H22z"/><line x1="11" y1="12" x2="25" y2="12"/><line x1="11" y1="16" x2="22" y2="16"/></svg>Keynote Speeches</div>
    <div class="skill"><svg width="48" height="42" fill="none" stroke="#fff" stroke-width="1.5"><path d="M14 40V30a14 14 0 1 1 20-4v14"/><circle cx="24" cy="18" r="5"/></svg>Elevator Pitches</div>
    <div class="skill"><svg width="48" height="42" fill="none" stroke="#fff" stroke-width="1.5"><rect x="18" y="4" width="18" height="34"/><rect x="30" y="14" width="12" height="24"/><line x1="22" y1="10" x2="32" y2="10"/><line x1="22" y1="16" x2="28" y2="16"/><circle cx="12" cy="30" r="7"/><line x1="4" y1="40" x2="44" y2="40"/></svg>Venture Capital<br>Presentations &amp; Decks</div>
    <div class="skill"><svg width="48" height="42" fill="none" stroke="#fff" stroke-width="1.5"><rect x="4" y="6" width="26" height="18"/><path d="M16 14h28v20h-6v6l-6-6H16z"/><line x1="22" y1="21" x2="38" y2="21"/><line x1="22" y1="27" x2="34" y2="27"/></svg>Convention &amp; Trade<br>Show Messaging</div>
  </div>
</section>

<section class="clients">
  <h2 class="section-title">OUR <b>CLIENTS</b></h2>
  <div class="rule" style="left:562px;top:115px;width:60px"></div>
  <svg class="arrow" style="left:86px" width="32" height="16" fill="none" stroke="#7d8aa3" stroke-width="1.8"><line x1="2" y1="8" x2="31" y2="8"/><polyline points="9,1 2,8 9,15"/></svg>
  <div class="client" style="left:194px"><i></i>Orchardly</div>
  <div class="client" style="left:350px"><i></i>Telvox</div>
  <div class="client" style="left:517px"><i></i>Indigo Troupe</div>
  <div class="client" style="left:682px"><i></i>Harbor Docks</div>
  <div class="client" style="left:855px"><i></i>Netrova</div>
  <div class="client" style="left:1022px"><i></i>Civitra Bank</div>
  <svg class="arrow" style="left:1095px" width="32" height="16" fill="none" stroke="#7d8aa3" stroke-width="1.8"><line x1="1" y1="8" x2="30" y2="8"/><polyline points="23,1 30,8 23,15"/></svg>
</section>

<section class="results">
  <div class="photo" role="img" aria-label="Hands on a keyboard beneath a glowing rising bar chart"></div>
  <svg class="edge" width="670" height="535" fill="none"><polyline points="536,0 651,268 536,535" stroke="#1f8ff0" stroke-width="5"/></svg>
  <h2 class="section-title">THE <b>RESULTS</b></h2>
  <div class="copy">
    <p>Whatever the message, and whatever the medium, we help clients establish a connection, make an impression, and drive audiences toward a predetermined course of action.</p>
    <p>This results in clear messaging, captivated audiences, and increased sales.</p>
  </div>
</section>

<footer class="site-footer">
  <div class="footer-divider" style="left:457px"></div>
  <div class="footer-divider" style="left:689px"></div>
  <div class="footer-divider" style="left:912px"></div>
  <div class="footer-mark" style="left:456px"></div>
  <div class="footer-mark" style="left:688px"></div>
  <div class="footer-mark" style="left:911px"></div>
  <div class="footer-brand">LANTERN &amp; LOOMLY</div>
  <p class="footer-about">Bright Demand partners with publishers to maximize their revenue potential by providing scalable and precision demand generation services.</p>
  <p class="footer-copy">© 2022 Lantern &amp; Loomly | All Rights Reserved</p>
  <div class="footer-col" style="left:503px"><h4>NAVIGATION</h4><a href="#">Home</a><a href="#">About Us</a><a href="#">Our Services</a></div>
  <div class="footer-col" style="left:735px"><h4>RESOURCES</h4><a href="#">Testimonials</a><a href="#">Team</a><a href="#">Contact Us</a></div>
  <div class="footer-col" style="left:948px"><h4>FOLLOW US</h4>
    <div class="social"><span><i></i>Friendsy</span><span><i></i>Chirply</span><span><i></i>Vidora</span><span><i></i>Pixgram</span></div>
  </div>
</footer>

</body>
</html>
```